Start-up needs a Web Design

We need a web design for a new Cleantech start-up based in California called "Fernwhistle".

Background info on our company:

Our company is active in the area of wastewater treatment. We have a patent-pending treatment system to clean the wastewater that is collected by vacuum trucks from septic tanks. The cleaned water can be re-used.

Our clients can save up to 90% of the wastewater discharge fees by using our system instead of just dumping it.

The two founders of the company have successfully launched other Cleantech and Medtech startups before.

We are offering our services in the United States, Canada, Mexico, and the whole of Southern America.
Updates

Dear Designers for Fernwhistle,

I have just updated the brief for the website of Fernwhistle.

The main change to the brief is that the main graphic / photo of the website should not be "How it works", but a photo of Truck / containter.

All the best, Marcus

Target Market(s)

n.a.

Industry/Entity Type

It Company

Requirements
Must have
• non
Nice to have
• non
Should not have
• n.a.

```html
<!DOCTYPE html>
<html lang="en">
<head>
<meta charset="utf-8">
<title>Fernwhistle — Wastewater Treatment</title>
<link rel="stylesheet" href="https://fonts.googleapis.com/css2?family=Open+Sans:ital,wght@0,400;0,600;0,700;0,800;1,400&display=swap">
<style>
:root{
  --blue:#1f77c4;
  --blue-dark:#0f4f8e;
  --blue-deep:#0b3d6e;
  --sky:#dcebf7;
  --sky-2:#eef5fb;
  --ink:#333a40;
  --muted:#6b747c;
  --line:#c9d6e2;
  --white:#ffffff;
  --page:#f3f6f9;
}
*{box-sizing:border-box;margin:0;padding:0}
html,body{width:872px;height:1200px;overflow:hidden}
body{font-family:"Open Sans",Arial,sans-serif;color:var(--ink);background:var(--white);font-size:11px;line-height:1.45}
.page{width:872px;height:1200px;position:relative}

/* header */
.site-header{height:130px;position:relative;background:var(--white)}
.brand{position:absolute;left:30px;top:22px;display:flex;align-items:center;gap:12px}
.brand-mark{width:34px;height:34px;border-radius:50%;background:var(--blue)}
.brand-name{font-weight:800;font-size:34px;color:var(--blue-deep);letter-spacing:-.5px}
.search{position:absolute;right:30px;top:14px;width:150px;height:22px;border:1px solid var(--line);border-radius:11px;display:flex;align-items:center;padding:0 10px;color:var(--muted);font-size:10px;justify-content:space-between}
.main-nav{position:absolute;right:30px;top:44px;display:flex;font-size:11px}
.main-nav a{color:var(--blue-dark);text-decoration:none;padding:0 8px;border-left:1px solid var(--line)}
.main-nav a:first-child{border-left:0;font-weight:700;color:var(--blue)}
.nav-rule{position:absolute;left:470px;right:30px;top:64px;height:2px;background:var(--blue)}

/* hero */
.hero{position:absolute;top:130px;left:0;width:872px;height:260px;background:linear-gradient(180deg,#2a8ad6,#1563ad)}
.hero-photo{position:absolute;left:30px;top:10px;width:440px;height:245px;background:linear-gradient(135deg,#b9c6d2,#7b8fa3 60%,#56697c)}
.hero-copy{position:absolute;left:508px;top:40px;width:320px;color:var(--white);font-size:21px;font-weight:600;line-height:1.3}
.btn-read{position:absolute;left:560px;top:170px;width:160px;height:40px;border-radius:20px;background:var(--blue-deep);color:var(--white);font-size:17px;font-weight:600;display:flex;align-items:center;justify-content:center;border:2px solid #4aa0e3}
.dots{position:absolute;left:490px;top:240px;display:flex;gap:5px}
.dots span{width:9px;height:9px;border-radius:50%;background:#9fc8ea}
.dots span:first-child{background:var(--white)}

/* main */
.content{position:absolute;top:400px;left:30px;width:812px;display:flex;gap:30px}
.intro{width:440px}
.intro h1{font-size:22px;font-weight:400;color:var(--blue);margin-bottom:6px}
.intro h1 b{color:var(--blue-deep);font-weight:800}
.intro p{font-size:10.5px;color:var(--muted);margin-bottom:10px}
.benefits{list-style:none;border-top:1px solid var(--line)}
.benefits li{display:flex;gap:8px;padding:7px 0;border-bottom:1px solid var(--line);font-size:10.5px;color:var(--ink)}
.benefits svg{flex:none;margin-top:2px}
.testimonial{margin-top:14px}
.testimonial h2{font-size:14px;font-style:italic;font-weight:600;color:var(--blue);margin-bottom:4px}
.testimonial blockquote{font-style:italic;font-size:10.5px;color:var(--muted);margin-bottom:6px}
.testimonial cite{font-style:normal;font-weight:700;font-size:11px}

.processes{flex:1;display:flex;flex-direction:column;gap:16px;padding-top:2px}
.process{position:relative;border:1px solid var(--line);border-radius:10px;background:var(--sky-2);height:126px;padding:24px 12px 10px}
.process h3{position:absolute;top:-12px;left:50%;transform:translateX(-50%);background:var(--white);border:1px solid var(--blue);color:var(--blue-dark);font-size:12px;font-weight:700;font-style:italic;padding:2px 16px;border-radius:12px;white-space:nowrap}
.flow{display:flex;align-items:center;justify-content:center;gap:8px}
.step{text-align:center;font-size:9.5px;color:var(--ink)}
.step-pic{width:90px;height:54px;border-radius:6px;background:linear-gradient(180deg,#d2dde8,#9fb3c6);margin-top:3px}
.flow-row{display:flex;align-items:center;gap:8px;justify-content:center;margin-top:6px}
.alt .flow{flex-direction:column;align-items:flex-start;gap:2px;padding-left:40px}
.alt .step{display:flex;align-items:center;gap:8px}
.alt .step-pic{width:70px;height:36px}

/* partners */
.partners{position:absolute;top:900px;left:30px;width:812px;height:76px;border:1px solid var(--line);border-radius:6px;display:flex;align-items:center;justify-content:space-around;padding:0 20px;background:var(--white)}
.partner{height:36px;border-radius:4px;background:#d9e1e8}

/* bottom */
.bottom{position:absolute;top:1000px;left:30px;width:812px;height:155px;border-top:2px solid var(--blue)}
.contact{position:absolute;left:0;top:12px;width:240px}
.contact h2{font-size:13px;font-style:italic;color:var(--blue);font-weight:600;margin-bottom:6px}
.contact .row{display:flex;align-items:flex-start;gap:8px;margin:5px 0;font-size:10.5px;font-weight:600}
.contact address{font-style:normal}
.foot-brand{position:absolute;left:300px;top:50px;display:flex;align-items:center;gap:12px}
.newsletter{position:absolute;right:0;top:14px;width:250px;height:128px;border-radius:8px;background:linear-gradient(180deg,#2a8ad6,#155fa8);padding:12px 16px;color:var(--white)}
.newsletter h2{font-size:19px;font-weight:400;margin-bottom:4px}
.newsletter p{font-size:9.5px;opacity:.9;margin-bottom:8px}
.newsletter .field{height:22px;background:var(--white);border-radius:3px;color:var(--muted);font-size:9.5px;padding:3px 8px;margin-bottom:7px}
.newsletter .btn{display:inline-block;background:var(--blue-deep);border-radius:3px;padding:3px 12px;font-size:10px;font-weight:600}

.site-footer{position:absolute;bottom:0;left:0;width:872px;height:34px;background:var(--blue-deep);color:#c6dcf0;font-size:9.5px;display:flex;align-items:center;justify-content:space-between;padding:0 30px}
.site-footer nav a{color:#c6dcf0;text-decoration:none;margin-left:10px}
</style>
</head>
<body>
<div class="page">
  <header class="site-header">
    <div class="brand"><span class="brand-mark"></span><span class="brand-name">Fernwhistle</span></div>
    <div class="search"><span>Search...</span>
      <svg width="10" height="10" viewBox="0 0 10 10"><circle cx="4" cy="4" r="3" fill="none" stroke="#6b747c" stroke-width="1.3"/><line x1="6.2" y1="6.2" x2="9" y2="9" stroke="#6b747c" stroke-width="1.3"/></svg>
    </div>
    <nav class="main-nav"><a href="#">Home</a><a href="#">About Us</a><a href="#">Our Services</a><a href="#">Our Partners</a><a href="#">Contact Us</a></nav>
    <div class="nav-rule"></div>
  </header>

  <section class="hero">
    <div class="hero-photo" role="img" aria-label="Photo of a vacuum truck with a container and two founders standing beside it"></div>
    <p class="hero-copy">We have a patent-pending system to clean wastewater that we built ourselves.</p>
    <a class="btn-read">Read More</a>
    <div class="dots"><span></span><span></span><span></span></div>
  </section>

  <main class="content">
    <div class="intro">
      <h1>Welcome to <b>Fernwhistle</b></h1>
      <p>Fernwhistle enables waste collection companies to easily clean their dirty wastewater. By cleaning their wastewater with our system, our clients can save up to 90% of the money they usually spend for their wastewater if they dump it at a communal treatment plant.</p>
      <ul class="benefits">
        <li><svg width="12" height="12" viewBox="0 0 12 12"><rect width="12" height="12" rx="2" fill="#1f77c4"/><path d="M3 6l2 2 4-4" stroke="#fff" stroke-width="1.6" fill="none"/></svg>We have spent many years treating wastewater from totally different industries. From this experience we know the best and easiest ways to treat wastewater.</li>
        <li><svg width="12" height="12" viewBox="0 0 12 12"><rect width="12" height="12" rx="2" fill="#1f77c4"/><path d="M3 6l2 2 4-4" stroke="#fff" stroke-width="1.6" fill="none"/></svg>We understand the market of wastewater treatment for small and mid-sized industrial companies and for waste collection companies.</li>
        <li><svg width="12" height="12" viewBox="0 0 12 12"><rect width="12" height="12" rx="2" fill="#1f77c4"/><path d="M3 6l2 2 4-4" stroke="#fff" stroke-width="1.6" fill="none"/></svg>We understand the problems that our clients have with their wastewater while having to run their daily business.</li>
        <li><svg width="12" height="12" viewBox="0 0 12 12"><rect width="12" height="12" rx="2" fill="#1f77c4"/><path d="M3 6l2 2 4-4" stroke="#fff" stroke-width="1.6" fill="none"/></svg>We have a patent-pending system to clean wastewater that we built ourselves.</li>
        <li><svg width="12" height="12" viewBox="0 0 12 12"><rect width="12" height="12" rx="2" fill="#1f77c4"/><path d="M3 6l2 2 4-4" stroke="#fff" stroke-width="1.6" fill="none"/></svg>We know how to operate and maintain our system with all kinds of different wastewater.</li>
      </ul>
      <div class="testimonial">
        <h2>What Our Clients Say's:</h2>
        <blockquote>“ Our trucks used to queue at the city plant every single day and the fees kept rising. Since switching to on-site treatment we re-use most of the water, our costs have dropped sharply and the crews finish routes much earlier than before. ”</blockquote>
        <cite>Happy Client | Designation</cite>
      </div>
    </div>

    <aside class="processes">
      <div class="process">
        <h3>Dump &amp; Pay Process</h3>
        <div class="flow">
          <div class="step">Waste Water<div class="step-pic" role="img" aria-label="Illustration of a septic tank with waste water"></div></div>
          <svg width="26" height="12" viewBox="0 0 26 12"><path d="M0 6h20M15 1l6 5-6 5" stroke="#1f77c4" stroke-width="2" fill="none"/></svg>
          <div class="step">Transport<div class="step-pic" role="img" aria-label="Illustration of a vacuum truck driving to a treatment plant"></div></div>
        </div>
      </div>
      <div class="process">
        <h3>Clean &amp; Re-Use</h3>
        <div class="flow">
          <div class="step">Waste Water<div class="step-pic" role="img" aria-label="Illustration of a septic tank with waste water"></div></div>
          <svg width="26" height="12" viewBox="0 0 26 12"><path d="M0 6h20M15 1l6 5-6 5" stroke="#1f77c4" stroke-width="2" fill="none"/></svg>
          <div class="step">Transport<div class="step-pic" role="img" aria-label="Illustration of a truck with the on-site cleaning container"></div></div>
        </div>
      </div>
      <div class="process alt">
        <h3>Alternate Process</h3>
        <div class="flow">
          <div class="step"><div class="step-pic" role="img" aria-label="Illustration of waste water tank"></div>Waste Water</div>
          <svg width="12" height="14" viewBox="0 0 12 14" style="margin-left:29px"><path d="M6 0v10M1 6l5 6 5-6" stroke="#1f77c4" stroke-width="2" fill="none"/></svg>
          <div class="step"><div class="step-pic" role="img" aria-label="Illustration of cleaned water tank"></div>Cleaned Water</div>
        </div>
      </div>
    </aside>
  </main>

  <section class="partners" aria-label="Partners">
    <div class="partner" style="width:80px"></div>
    <div class="partner" style="width:90px"></div>
    <div class="partner" style="width:70px"></div>
    <div class="partner" style="width:44px;border-radius:50%;height:44px"></div>
    <div class="partner" style="width:84px"></div>
    <div class="partner" style="width:70px"></div>
    <div class="partner" style="width:86px"></div>
  </section>

  <section class="bottom">
    <div class="contact">
      <h2>Contact Details</h2>
      <div class="row"><svg width="12" height="12" viewBox="0 0 12 12"><rect x="2" y="0" width="8" height="12" rx="1.5" fill="#1f77c4"/><rect x="3.5" y="1.5" width="5" height="7" fill="#fff"/></svg>555 014 2206</div>
      <div class="row"><svg width="12" height="12" viewBox="0 0 12 12"><rect x="0" y="3" width="12" height="7" rx="1" fill="#1f77c4"/><rect x="3" y="0" width="6" height="4" fill="#1f77c4"/></svg>555 014 2207</div>
      <div class="row"><svg width="12" height="12" viewBox="0 0 12 12"><path d="M6 0a4 4 0 0 1 4 4c0 3-4 8-4 8S2 7 2 4a4 4 0 0 1 4-4z" fill="#1f77c4"/><circle cx="6" cy="4" r="1.5" fill="#fff"/></svg><address>Dummy Area, Dummy Block,<br>Dummy City, Dummy Country</address></div>
    </div>
    <div class="foot-brand"><span class="brand-mark"></span><span class="brand-name">Fernwhistle</span></div>
    <div class="newsletter">
      <h2>Newsletter Signup</h2>
      <p>Subscribe Now and Get Latest Updates</p>
      <div class="field">Enter Email Address...</div>
      <span class="btn">Subscribe Now</span>
    </div>
  </section>

  <footer class="site-footer">
    <span>Copyright ©2011 Brightwater Holdings Inc. All rights reserved.</span>
    <nav><a href="#">Home</a>|<a href="#">About Us</a>|<a href="#">Our Services</a>|<a href="#">Our Partners</a>|<a href="#">Contact Us</a></nav>
  </footer>
</div>
</body>
</html>
```